Fireworks company

COLORFUL design, incorporating logo (attached).
Information to be included:
PO BOX 4829
Marlow Vale 3891
Ph 03 5461 8237
Fax 03 5387 9216
Email sales@brindarockets.com.au
Web www.brindarockets.com.au

Check out our website for more inspiration? :-)

```html
<!DOCTYPE html>
<html lang="en">
<head>
<meta charset="utf-8">
<title>Brinda Rockets Letterhead</title>
<link rel="stylesheet" href="https://fonts.googleapis.com/css2?family=Roboto+Slab:wght@700&family=Roboto:wght@700&display=swap">
<style>
  :root {
    --frame: #f6b21b;
    --paper: #ffffff;
    --band: #0b0b0b;
    --orange: #f47a16;
    --flame: #f9a01b;
    --red: #e0321a;
    --text-light: #f2f2f2;
  }
  * { margin: 0; padding: 0; box-sizing: border-box; }
  html, body { width: 847px; height: 1200px; overflow: hidden; background: #e9e9e9; }
  .letterhead {
    position: relative;
    width: 847px; height: 1200px;
    background: var(--frame);
    padding: 22px;
  }
  .sheet {
    position: relative;
    width: 100%; height: 100%;
    background: var(--paper);
    overflow: hidden;
  }
  .masthead {
    position: absolute; left: 0; top: 0;
    width: 100%; height: 225px;
    background: var(--band);
  }
  .burst-cluster {
    position: absolute; left: 18px; top: 18px;
    width: 120px; height: 130px;
    border-radius: 50%;
    background: radial-gradient(circle at 50% 50%, #ff5a2a 0%, #b31c14 40%, #3a0906 70%, var(--band) 100%);
  }
  .burst-photo {
    position: absolute; right: 22px; top: 28px;
    width: 140px; height: 125px;
    border-radius: 50%;
    background: radial-gradient(circle, #ff6fa0 0%, #c3185c 40%, #3c0620 70%, var(--band) 100%);
  }
  .brand-name {
    position: absolute; left: 158px; top: 48px;
    width: 280px;
    font-family: 'Roboto Slab', serif;
    font-weight: 700;
    font-size: 50px; line-height: 1.08;
    color: var(--orange);
  }
  .divider {
    position: absolute; left: 455px; top: 36px;
    width: 3px; height: 130px;
    background: var(--text-light);
  }
  .postal {
    position: absolute; left: 472px; top: 42px;
    font-family: 'Roboto Slab', serif;
    font-weight: 700;
    font-size: 15px; line-height: 25px;
    color: var(--text-light);
  }
  .postal .label { display: inline-block; width: 62px; }
  .online {
    position: absolute; left: 70px; top: 184px;
    font-family: 'Roboto', sans-serif;
    font-weight: 700;
    font-size: 14px;
    color: var(--text-light);
    display: flex; gap: 22px;
  }
  .online .label { color: var(--red); margin-right: 6px; }
  .online .sep { color: var(--flame); }
  .stripe-thick {
    position: absolute; left: 0; top: 225px;
    width: 100%; height: 12px;
    background: linear-gradient(90deg, var(--orange), var(--flame));
  }
  .stripe-thin {
    position: absolute; left: 0; top: 250px;
    width: 100%; height: 3px;
    background: var(--red);
  }
  .footer-wave {
    position: absolute; left: 0; bottom: 0;
    width: 100%; height: 190px;
  }
</style>
</head>
<body>
  <main class="letterhead">
    <section class="sheet">
      <header class="masthead">
        <div class="burst-cluster" role="img" aria-label="Photograph of red fireworks bursting"></div>
        <h1 class="brand-name">BRINDA ROCKETS</h1>
        <div class="divider"></div>
        <address class="postal" style="font-style: normal;">
          <div>PO BOX 4829</div>
          <div>Marlow Vale 3891</div>
          <div><span class="label">Phone:</span>03 5461 8237</div>
          <div><span class="label">Fax:</span>03 5387 9216</div>
        </address>
        <div class="burst-photo" role="img" aria-label="Photograph of a pink firework burst"></div>
        <p class="online">
          <span><span class="label">Email:</span>sales@brindarockets.com.au</span>
          <span class="sep">•</span>
          <span><span class="label">Web:</span>www.brindarockets.com.au</span>
        </p>
      </header>
      <div class="stripe-thick"></div>
      <div class="stripe-thin"></div>

      <svg class="footer-wave" viewBox="0 0 803 190" preserveAspectRatio="none" aria-hidden="true">
        <defs>
          <linearGradient id="waveGlow" x1="0" y1="0" x2="0" y2="1">
            <stop offset="0" stop-color="#ffd23a"/>
            <stop offset="1" stop-color="#f47a16"/>
          </linearGradient>
        </defs>
        <path d="M0 40 C200 120 520 150 803 70 L803 190 L0 190 Z" fill="#fde3b0"/>
        <path d="M0 80 C220 150 540 160 803 95 L803 190 L0 190 Z" fill="url(#waveGlow)"/>
        <path d="M0 120 C260 175 560 170 803 125 L803 190 L0 190 Z" fill="#f47a16"/>
        <path d="M0 80 C220 150 540 160 803 95" fill="none" stroke="#ffffff" stroke-width="3" opacity="0.8"/>
      </svg>
    </section>
  </main>
</body>
</html>
```